Restaurant Facility Equipment & Store Maintenance/

I need a flyer showing commercial/industrial kitchen equipment photos we work on Hot Equipment & Cold Equipment and offer many services. see attached highlights

```html
<!DOCTYPE html>
<html lang="en">
<head>
<meta charset="utf-8">
<title>Restaurant Facility Equipment &amp; Store Maintenance Flyer</title>
<link href="https://fonts.googleapis.com/css2?family=Arimo:wght@400;700&display=swap" rel="stylesheet">
<style>
  :root {
    --orange: #f47a1f;
    --orange-deep: #e0620f;
    --ink: #1f1f1f;
    --white: #ffffff;
    --paper: #f7f7f6;
  }
  * { margin: 0; padding: 0; box-sizing: border-box; }
  html, body { width: 849px; height: 1200px; overflow: hidden; background: var(--white); }
  .flyer {
    position: relative; width: 849px; height: 1200px; overflow: hidden;
    font-family: "Arimo", Arial, sans-serif; background: var(--white);
  }
  .photo-dining {
    position: absolute; left: 0; top: 0; width: 849px; height: 640px;
    background: linear-gradient(120deg, #4a423b 0%, #2a2521 45%, #3b3530 70%, #7a746e 100%);
  }
  .photo-tables {
    position: absolute; left: 0; top: 540px; width: 849px; height: 620px;
    background: linear-gradient(160deg, #ffffff 0%, #efefed 45%, #dcdbd8 80%, #ebebea 100%);
  }
  .waves { position: absolute; inset: 0; width: 849px; height: 1200px; }
  .intro {
    position: absolute; left: 175px; top: 78px; width: 590px; color: var(--white);
  }
  .intro h1 {
    font-size: 26px; line-height: 1.06; font-weight: 700; letter-spacing: -0.2px;
  }
  .intro p {
    margin-top: 8px; font-size: 14.5px; line-height: 1.17; font-weight: 400;
  }
  .services {
    position: absolute; left: 142px; top: 658px; width: 630px; list-style: none;
  }
  .services li {
    position: relative; padding-left: 33px; margin-bottom: 9.5px;
    font-size: 15px; line-height: 18px; font-weight: 700; color: var(--ink);
  }
  .services li .tick {
    position: absolute; left: 0; top: -1px; width: 20px; height: 20px;
  }
  .footer {
    position: absolute; left: 0; bottom: 0; width: 849px; height: 34px;
    background: var(--orange); color: var(--white);
    display: flex; justify-content: center; align-items: center; gap: 34px;
    font-size: 10px; font-weight: 700; letter-spacing: 0.6px;
  }
</style>
</head>
<body>
<div class="flyer">
  <div class="photo-dining" role="img" aria-label="Photo of a modern restaurant dining room with a dark stone wall and white chairs"></div>
  <div class="photo-tables" role="img" aria-label="Soft faded photo of white restaurant tables and chairs"></div>

  <svg class="waves" viewBox="0 0 849 1200" xmlns="http://www.w3.org/2000/svg" aria-hidden="true">
    <path class="wave-orange-right" d="M849 470 C720 490 600 540 500 640 L849 640 Z" fill="var(--orange)"/>
    <path class="wave-white" d="M0 385 C180 470 360 440 520 480 C650 520 760 600 849 585 L849 1200 L0 1200 Z" fill="var(--paper)" opacity="0.9"/>
    <path class="wave-orange-left" d="M0 200 C110 205 190 285 215 370 C160 415 80 420 0 405 Z" fill="var(--orange)"/>
    <path class="wave-orange-tail" d="M215 370 C245 430 225 490 120 535 C175 480 195 430 188 388 Z" fill="var(--orange-deep)"/>
  </svg>

  <header class="intro">
    <h1>Installation, Rebuilds, OSHA Inspection, and Preventive Maintenance Services for Denver Metro and Surrounding Areas.</h1>
    <p>"We handle everything from the front door to the back door." We offer hot and cold equipment repair, cleaning, maintenance, handyman work, drywall, painting, door closers, floors, and ceiling tiles. For any need in your restaurant, call us and we will send a skilled technician to manage all your commercial and industrial facility requirements.</p>
  </header>

  <ul class="services">
    <li><svg class="tick" viewBox="0 0 21 21"><circle cx="10.5" cy="10.5" r="10.5" fill="var(--orange)"/><path d="M5.5 11 L9 14.5 L15.5 7" stroke="#fff" stroke-width="2.4" fill="none" stroke-linecap="round" stroke-linejoin="round"/></svg>CKTA Certified Technicians</li>
    <li><svg class="tick" viewBox="0 0 21 21"><circle cx="10.5" cy="10.5" r="10.5" fill="var(--orange)"/><path d="M5.5 11 L9 14.5 L15.5 7" stroke="#fff" stroke-width="2.4" fill="none" stroke-linecap="round" stroke-linejoin="round"/></svg>Round-the-clock emergency services</li>
    <li><svg class="tick" viewBox="0 0 21 21"><circle cx="10.5" cy="10.5" r="10.5" fill="var(--orange)"/><path d="M5.5 11 L9 14.5 L15.5 7" stroke="#fff" stroke-width="2.4" fill="none" stroke-linecap="round" stroke-linejoin="round"/></svg>Customers who subscribe to preventive maintenance services receive a reduced rate on hourly labor charges.</li>
    <li><svg class="tick" viewBox="0 0 21 21"><circle cx="10.5" cy="10.5" r="10.5" fill="var(--orange)"/><path d="M5.5 11 L9 14.5 L15.5 7" stroke="#fff" stroke-width="2.4" fill="none" stroke-linecap="round" stroke-linejoin="round"/></svg>Original equipment manufacturer (OEM) parts</li>
    <li><svg class="tick" viewBox="0 0 21 21"><circle cx="10.5" cy="10.5" r="10.5" fill="var(--orange)"/><path d="M5.5 11 L9 14.5 L15.5 7" stroke="#fff" stroke-width="2.4" fill="none" stroke-linecap="round" stroke-linejoin="round"/></svg>30-day warranty on all OEM parts installed</li>
    <li><svg class="tick" viewBox="0 0 21 21"><circle cx="10.5" cy="10.5" r="10.5" fill="var(--orange)"/><path d="M5.5 11 L9 14.5 L15.5 7" stroke="#fff" stroke-width="2.4" fill="none" stroke-linecap="round" stroke-linejoin="round"/></svg>Equipment Cleaning &amp; Rebuilds</li>
    <li><svg class="tick" viewBox="0 0 21 21"><circle cx="10.5" cy="10.5" r="10.5" fill="var(--orange)"/><path d="M5.5 11 L9 14.5 L15.5 7" stroke="#fff" stroke-width="2.4" fill="none" stroke-linecap="round" stroke-linejoin="round"/></svg>Used equipment available for purchase or rental</li>
    <li><svg class="tick" viewBox="0 0 21 21"><circle cx="10.5" cy="10.5" r="10.5" fill="var(--orange)"/><path d="M5.5 11 L9 14.5 L15.5 7" stroke="#fff" stroke-width="2.4" fill="none" stroke-linecap="round" stroke-linejoin="round"/></svg>Specialized Programs for Preventive Maintenance of Equipment</li>
    <li><svg class="tick" viewBox="0 0 21 21"><circle cx="10.5" cy="10.5" r="10.5" fill="var(--orange)"/><path d="M5.5 11 L9 14.5 L15.5 7" stroke="#fff" stroke-width="2.4" fill="none" stroke-linecap="round" stroke-linejoin="round"/></svg>Installation and Repair of Restaurant Equipment</li>
    <li><svg class="tick" viewBox="0 0 21 21"><circle cx="10.5" cy="10.5" r="10.5" fill="var(--orange)"/><path d="M5.5 11 L9 14.5 L15.5 7" stroke="#fff" stroke-width="2.4" fill="none" stroke-linecap="round" stroke-linejoin="round"/></svg>Repair or replace restaurant furniture</li>
    <li><svg class="tick" viewBox="0 0 21 21"><circle cx="10.5" cy="10.5" r="10.5" fill="var(--orange)"/><path d="M5.5 11 L9 14.5 L15.5 7" stroke="#fff" stroke-width="2.4" fill="none" stroke-linecap="round" stroke-linejoin="round"/></svg>Comprehensive licensed electrical contractor services for both and exterior projects, including lighting system upgrades.</li>
    <li><svg class="tick" viewBox="0 0 21 21"><circle cx="10.5" cy="10.5" r="10.5" fill="var(--orange)"/><path d="M5.5 11 L9 14.5 L15.5 7" stroke="#fff" stroke-width="2.4" fill="none" stroke-linecap="round" stroke-linejoin="round"/></svg>Building Graffiti Removal Services</li>
    <li><svg class="tick" viewBox="0 0 21 21"><circle cx="10.5" cy="10.5" r="10.5" fill="var(--orange)"/><path d="M5.5 11 L9 14.5 L15.5 7" stroke="#fff" stroke-width="2.4" fill="none" stroke-linecap="round" stroke-linejoin="round"/></svg>Hot &amp; Cold Equipment</li>
    <li><svg class="tick" viewBox="0 0 21 21"><circle cx="10.5" cy="10.5" r="10.5" fill="var(--orange)"/><path d="M5.5 11 L9 14.5 L15.5 7" stroke="#fff" stroke-width="2.4" fill="none" stroke-linecap="round" stroke-linejoin="round"/></svg>Food Service Trucks</li>
    <li><svg class="tick" viewBox="0 0 21 21"><circle cx="10.5" cy="10.5" r="10.5" fill="var(--orange)"/><path d="M5.5 11 L9 14.5 L15.5 7" stroke="#fff" stroke-width="2.4" fill="none" stroke-linecap="round" stroke-linejoin="round"/></svg>We repair floors, walls, counters, décor, signage, parking lots, dumpsters, and more. If you have it, we probably fix it.</li>
  </ul>

  <footer class="footer">
    <span class="footer-web">WWW.FRONTTOBACKPRO.COM</span>
    <span class="footer-phone">(555) 014 2290</span>
  </footer>
</div>
</body>
</html>
```